Business card por a urban DJ, up scale audience target

Need a sober design, modern, conservative colors but i can consider some options, y play rnb, hip hop, EDM and top40.

Business card for contact and personal info, double sided, use logo attrached please; im 42 so i need a card acording to my age an target audience.

Target Market(s)

Adult people, up scale audience

Industry/Entity Type

Music Download

Contact Information for Business Card

Cel (318) 5024471963 www.kelvarodun.com

Requirements
Must have
• open mind
Nice to have
• open mind
Should not have
• DJ

```html
<!DOCTYPE html>
<html lang="en">
<head>
<meta charset="utf-8">
<title>KELVA — Business Card</title>
<link rel="stylesheet" href="https://fonts.googleapis.com/css2?family=Open+Sans:wght@400;700;800&display=swap">
<style>
  :root {
    --stage: #3b3b3b;
    --card-light: #ffffff;
    --card-dark: #151515;
    --ink: #231f20;
    --ink-soft: #333333;
    --paper: #ffffff;
  }
  * { margin: 0; padding: 0; box-sizing: border-box; }
  html, body { width: 1200px; height: 720px; overflow: hidden; }
  body {
    background: var(--stage);
    font-family: "Open Sans", Arial, sans-serif;
    display: flex;
    align-items: center;
    justify-content: center;
    gap: 60px;
  }
  .card {
    width: 500px;
    height: 286px;
    display: flex;
    flex-direction: column;
    align-items: center;
    justify-content: center;
    box-shadow: 0 10px 30px rgba(0,0,0,0.35);
  }
  .card--front { background: var(--card-light); color: var(--ink); }
  .card--back { background: var(--card-dark); color: var(--paper); }
  .brand {
    display: flex;
    align-items: center;
    gap: 12px;
    font-weight: 800;
    letter-spacing: 4px;
    line-height: 1;
  }
  .brand__mark { width: 16px; height: 16px; background: currentColor; }
  .card--front .brand { font-size: 58px; margin-bottom: 30px; }
  .card--back .brand { font-size: 76px; }
  .contact {
    display: flex;
    flex-direction: column;
    align-items: center;
    gap: 4px;
    color: var(--ink-soft);
    font-size: 15px;
    font-weight: 400;
  }
  .contact__icon { width: 20px; height: 20px; margin-bottom: 4px; }
  .contact__web strong { font-weight: 700; }
</style>
</head>
<body>
  <section class="card card--front">
    <div class="brand"><span class="brand__mark"></span>KELVA</div>
    <div class="contact">
      <svg class="contact__icon" viewBox="0 0 20 20" aria-hidden="true">
        <rect width="20" height="20" rx="2" fill="#231f20"/>
        <path d="M4 8 Q10 3 16 8 L14 10 L12 8.5 L8 8.5 L6 10 Z" fill="#fff"/>
        <rect x="6" y="10" width="8" height="6" rx="1" fill="#fff"/>
        <circle cx="10" cy="13" r="1.6" fill="#231f20"/>
      </svg>
      <span class="contact__phone">(318) 5024471963</span>
      <span class="contact__web">www.<strong>kelvarodun</strong>.com</span>
    </div>
  </section>
  <section class="card card--back">
    <div class="brand"><span class="brand__mark"></span>KELVA</div>
  </section>
</body>
</html>
```